Banner Ad Design Project

We are a SEO company and need a banner design for our new service, the highlights being:

- Pay Per Performance SEO service
- Guaranteed Zumbly page 1 ranking
- Only $197 per month (+ performance bonus)

Can be all on one static banner or made into an animated GIF - designers choice...

Site URL (not up yet) will be RankNest412.com (by velHelm) - this is a spinoff site of our existing business, velHelm LLC - logo attached and should be included on the banner.

Industry/Entity Type

Business

Requirements
Must have
• Banner delivered in multiple sizes:
- 200 x 200
- 250 x 250
- 300 x 250
- 336 x 280
- 468 x 60
- 728 x 90
- 120 x 600
- 160 x 600

```html
<!DOCTYPE html>
<html lang="en">
<head>
<meta charset="utf-8">
<title>velHelm – Pay Per Performance SEO Banners</title>
<link rel="stylesheet" href="https://fonts.googleapis.com/css2?family=Bebas+Neue&family=Oswald:wght@500;600&family=Ubuntu:wght@500&display=swap">
<style>
  :root {
    --page-bg: #ffffff;
    --banner-deep: #0b3a7e;
    --banner-mid: #1459a8;
    --banner-light: #1f6fc0;
    --badge-top: #eaef3a;
    --badge-bottom: #8fb61c;
    --badge-edge: #6f8f12;
    --headline-blue: #1d3c8f;
    --text-white: #ffffff;
    --logo-green: #8cc63f;
    --curl-light: #ffffff;
    --curl-shade: #c9ccd2;
  }
  * { margin: 0; padding: 0; box-sizing: border-box; }
  html, body {
    width: 1200px; height: 1007px; overflow: hidden;
    background: var(--page-bg);
  }
  .canvas { position: relative; width: 1200px; height: 1007px; }

  .banner {
    position: absolute; overflow: hidden;
    background:
      radial-gradient(ellipse at 60% 45%, var(--banner-light) 0%, var(--banner-mid) 40%, var(--banner-deep) 100%);
  }
  .banner--square { left: 266px; top: 79px; width: 698px; height: 581px; }
  .banner--leader { left: 38px; top: 795px; width: 1091px; height: 140px; }

  .badge {
    position: absolute; border-radius: 18px;
    background: linear-gradient(to bottom, var(--badge-top) 0%, #cddc2c 55%, var(--badge-bottom) 100%);
    box-shadow: 0 6px 0 var(--badge-edge), 0 10px 18px rgba(0,0,0,.35);
    text-align: center; font-family: "Bebas Neue", "Oswald", sans-serif;
  }
  .banner--square .badge { left: 40px; top: 31px; width: 615px; height: 240px; }
  .banner--leader .badge { left: 87px; top: 9px; width: 315px; height: 120px; border-radius: 10px; box-shadow: 0 4px 0 var(--badge-edge), 0 6px 10px rgba(0,0,0,.35); }

  .badge__headline { color: var(--headline-blue); line-height: 1; display: block; }
  .badge__sub {
    color: var(--text-white); line-height: 1; display: block;
    text-shadow: 0 2px 3px rgba(0,0,0,.35);
  }
  .banner--square .badge__headline { font-size: 148px; margin-top: 14px; letter-spacing: 1px; }
  .banner--square .badge__sub { font-size: 70px; margin-top: -6px; }
  .banner--leader .badge__headline { font-size: 72px; margin-top: 8px; }
  .banner--leader .badge__sub { font-size: 34px; margin-top: -4px; }

  .offer {
    position: absolute; color: var(--text-white);
    font-family: "Bebas Neue", "Oswald", sans-serif; line-height: 1.15;
  }
  .banner--square .offer { left: 0; width: 100%; top: 298px; text-align: center; font-size: 36px; }
  .banner--leader .offer { left: 422px; top: 42px; }
  .banner--leader .offer__service { font-size: 28px; display: block; }
  .banner--leader .offer__price { font-size: 18px; display: block; }

  .brand {
    position: absolute; display: flex; align-items: center; gap: 12px;
    white-space: nowrap;
    color: var(--text-white); font-family: "Ubuntu", sans-serif; font-weight: 500;
    line-height: 1;
  }
  .brand__dot { border-radius: 50%; background: var(--logo-green); flex: none; }
  .banner--square .brand { right: 38px; top: 442px; font-size: 60px; }
  .banner--square .brand__dot { width: 96px; height: 96px; }
  .banner--leader .brand { right: 24px; top: 22px; font-size: 50px; }
  .banner--leader .brand__dot { width: 94px; height: 94px; }

  .curl { position: absolute; left: 0; bottom: 0; }
</style>
</head>
<body>
<main class="canvas">

  <section class="banner banner--square" aria-label="velHelm SEO banner, square">
    <div class="badge">
      <span class="badge__headline">Guaranteed</span>
      <span class="badge__sub">Zumbly Page 1 Ranking</span>
    </div>
    <p class="offer">Pay Per Performance SEO Service<br>Only $197 Per Month (+ Performance Bonus)</p>
    <div class="brand"><span class="brand__dot"></span>velHelm</div>
    <svg class="curl" width="150" height="150" viewBox="0 0 150 150" aria-hidden="true">
      <defs>
        <linearGradient id="curlFoldSq" x1="0" y1="0" x2="1" y2="1">
          <stop offset="0" stop-color="var(--curl-shade)"/>
          <stop offset=".55" stop-color="var(--curl-light)"/>
          <stop offset="1" stop-color="#e6e8ec"/>
        </linearGradient>
      </defs>
      <path d="M0 150 L0 20 C40 30 90 20 110 0 C95 40 110 110 150 150 Z" fill="var(--page-bg)"/>
      <path d="M0 20 C40 30 90 20 110 0 C95 40 110 110 150 150 C80 130 20 90 0 20 Z" fill="url(#curlFoldSq)"/>
    </svg>
  </section>

  <section class="banner banner--leader" aria-label="velHelm SEO banner, leaderboard">
    <div class="badge">
      <span class="badge__headline">Guaranteed</span>
      <span class="badge__sub">Zumbly Page 1 Ranking</span>
    </div>
    <p class="offer">
      <span class="offer__service">Pay Per Performance SEO Service</span>
      <span class="offer__price">Only $197 Per Month (+ Performance Bonus)</span>
    </p>
    <div class="brand"><span class="brand__dot"></span>velHelm</div>
    <svg class="curl" width="56" height="56" viewBox="0 0 150 150" aria-hidden="true">
      <defs>
        <linearGradient id="curlFoldLb" x1="0" y1="0" x2="1" y2="1">
          <stop offset="0" stop-color="var(--curl-shade)"/>
          <stop offset=".55" stop-color="var(--curl-light)"/>
          <stop offset="1" stop-color="#e6e8ec"/>
        </linearGradient>
      </defs>
      <path d="M0 150 L0 20 C40 30 90 20 110 0 C95 40 110 110 150 150 Z" fill="var(--page-bg)"/>
      <path d="M0 20 C40 30 90 20 110 0 C95 40 110 110 150 150 C80 130 20 90 0 20 Z" fill="url(#curlFoldLb)"/>
    </svg>
  </section>

</main>
</body>
</html>
```